Brightpath Home & Upkeep Services, are a company that offers a 'one stop shop' pre-move clean up a

I have already selected a logo which I would like on the front of the business cards along with phone numbers, web address and email which are:
0419586402
www.brightpathhome.com.au
brightpathandupkeep@mailnest.com

On the back of the card I would like to list some of the types of service we offer (clean - move - repairs/maintenance) which are:
CLEAN - windows, gutters, solar panels, driveways/paths, carpets.
MOVE - Small/medium size house/office moves, large item pick-up & delivery, yard clean-up and removal.
General maintenance and repairs.

I would like the blue logo on a gray background.

Thanks

```html
<!DOCTYPE html>
<html lang="en">
<head>
<meta charset="utf-8">
<title>Brightpath Home &amp; Upkeep Services – Business Card</title>
<link href="https://fonts.googleapis.com/css2?family=Open+Sans:wght@400;600;800&display=swap" rel="stylesheet">
<style>
  :root {
    --page-bg: #e6e6e6;
    --card-light: #f6f6f7;
    --card-mid: #dcdcde;
    --card-dark: #bfc0c3;
    --brand-blue: #2f78c4;
    --ink: #231f20;
    --ink-soft: #3a3a3c;
  }
  * { box-sizing: border-box; margin: 0; padding: 0; }
  html, body {
    width: 1200px; height: 805px; overflow: hidden;
    background: var(--page-bg);
    font-family: "Open Sans", Arial, sans-serif;
  }
  .canvas { position: relative; width: 1200px; height: 805px; }

  .card {
    position: absolute;
    width: 540px; height: 310px;
    border-radius: 4px;
    box-shadow: 0 6px 18px rgba(0,0,0,0.25);
    overflow: hidden;
  }
  .card--front {
    left: 70px; top: 80px;
    background: linear-gradient(160deg, var(--card-dark) 0%, var(--card-mid) 40%, var(--card-light) 100%);
  }
  .card--back {
    left: 590px; top: 410px;
    background: radial-gradient(ellipse at 45% 40%, var(--card-light) 0%, var(--card-mid) 55%, var(--card-dark) 100%);
  }

  .brand-name {
    display: flex; align-items: center; justify-content: center; gap: 12px;
    color: var(--brand-blue);
    font-weight: 800;
    font-size: 30px;
    line-height: 1.1;
    text-align: center;
  }
  .brand-name__mark {
    width: 18px; height: 18px; border-radius: 50%;
    background: var(--brand-blue); flex: none;
  }
  .card--front .brand-name { position: absolute; left: 30px; right: 30px; top: 78px; }
  .card--back .brand-name { position: absolute; left: 30px; right: 30px; top: 42px; }

  .contact {
    position: absolute; left: 0; right: 0; bottom: 44px;
    display: flex; justify-content: center; align-items: center;
    font-size: 13px; color: var(--ink-soft);
  }
  .contact__phone { display: flex; align-items: center; gap: 7px; padding-right: 22px; }
  .contact__divider { width: 1px; height: 56px; background: #ffffff; box-shadow: 1px 0 0 #b5b6b9; }
  .contact__online { display: flex; flex-direction: column; gap: 12px; padding-left: 22px; }
  .contact__line { display: flex; align-items: center; gap: 7px; }
  .icon { width: 13px; height: 13px; flex: none; }

  .services { position: absolute; left: 0; right: 0; top: 150px; text-align: center; }
  .services__title {
    color: var(--brand-blue);
    font-weight: 600; font-size: 20px;
    letter-spacing: 6px;
    margin-bottom: 10px;
  }
  .services__list { list-style: none; color: var(--ink); font-weight: 600; font-size: 17px; line-height: 1.45; }
  .services__list li span + span { margin-left: 18px; }
  .bullet { color: var(--brand-blue); }
</style>
</head>
<body>
<div class="canvas">

  <section class="card card--front" aria-label="Business card front">
    <div class="brand-name">
      <span class="brand-name__mark" aria-hidden="true"></span>
      <span>Brightpath Home &amp;<br>Upkeep Services</span>
    </div>

    <div class="contact">
      <div class="contact__phone">
        <svg class="icon" viewBox="0 0 16 16" aria-hidden="true">
          <circle cx="8" cy="8" r="8" fill="#2f78c4"/>
          <path d="M5.2 4.2l1.4-.4.8 2-1 .7c.5 1.1 1.2 1.9 2.2 2.4l.7-1 2 .8-.4 1.4c-3.2 0-5.7-2.7-5.7-5.9z" fill="#fff"/>
        </svg>
        <span>0419586402</span>
      </div>
      <div class="contact__divider" aria-hidden="true"></div>
      <div class="contact__online">
        <div class="contact__line">
          <svg class="icon" viewBox="0 0 16 16" aria-hidden="true">
            <circle cx="8" cy="8" r="8" fill="#2f78c4"/>
            <rect x="4" y="5" width="8" height="6" fill="#fff"/>
            <path d="M4 5l4 3.2L12 5" fill="none" stroke="#2f78c4" stroke-width="1"/>
          </svg>
          <span>brightpathandupkeep@mailnest.com</span>
        </div>
        <div class="contact__line">
          <svg class="icon" viewBox="0 0 16 16" aria-hidden="true">
            <circle cx="8" cy="8" r="8" fill="#2f78c4"/>
            <circle cx="8" cy="8" r="4.5" fill="none" stroke="#fff" stroke-width="1"/>
            <ellipse cx="8" cy="8" rx="2" ry="4.5" fill="none" stroke="#fff" stroke-width="1"/>
            <line x1="3.5" y1="8" x2="12.5" y2="8" stroke="#fff" stroke-width="1"/>
          </svg>
          <span>www.brightpathhome.com.au</span>
        </div>
      </div>
    </div>
  </section>

  <section class="card card--back" aria-label="Business card back">
    <div class="brand-name">
      <span class="brand-name__mark" aria-hidden="true"></span>
      <span>Brightpath Home &amp;<br>Upkeep Services</span>
    </div>

    <div class="services">
      <h2 class="services__title">Services we offer</h2>
      <ul class="services__list">
        <li><span><span class="bullet">•</span> Clean</span><span><span class="bullet">•</span> Move</span></li>
        <li><span class="bullet">•</span> General maintenance and repairs.</li>
      </ul>
    </div>
  </section>

</div>
</body>
</html>
```